Investment Management Firm Power point template

Harrowgate Capital is a real estate investment firm focused on buying commercial office and residential property in the UK. We produce powerpoint presentations for our Board of Directors, Investment Committee and also to external investors.

We are looking for a powerpoint design template which we can use for future presentations which provide a professional look and feel.

Our current website: http://www.harrowgatecapital.co.uk/

Target Market(s)

Institution Investors, Board of Directors, Professionals

Industry/Entity Type

Real Estate

Requirements
Must have
• Leverage off the current logo and colour scheme. However, does not have to purely rely on this colour scheme.
• - Title page
• - Content Page
• - Slide where graphs can be incorporated
• - Slide where photos can be incorporated
• - Slide of UK Map which can show where the property portfolio is currently located
• - Other slides incorporating smart art or other designs that can be used for future presentations
Nice to have
• An example of graphics that we would love to have in the powerpoint pack which we can easily edit has been attached

```html
<!DOCTYPE html>
<html lang="en">
<head>
<meta charset="utf-8">
<title>Ashcombe Holdings – Slide</title>
<link rel="stylesheet" href="https://fonts.googleapis.com/css2?family=Titillium+Web:wght@300;400;600;700&display=swap">
<style>
  :root {
    --brand-blue: #1f5d8c;
    --ink: #222222;
    --body-text: #555555;
    --footer-blue: #276a99;
    --teal: #3a8fae;
    --mid-gray: #7a7a7a;
    --dark-gray: #555555;
    --navy: #1f4f80;
    --ocean: #0e5a85;
    --deep-teal: #05496b;
    --charcoal: #2b2b2b;
    --inner-gray: #777777;
    --mark-blue: #2e5a7a;
    --white: #ffffff;
  }
  * { margin: 0; padding: 0; box-sizing: border-box; }
  html, body { width: 1200px; height: 900px; overflow: hidden; }
  body { font-family: "Titillium Web", sans-serif; background: var(--white); }
  .slide { position: relative; width: 1200px; height: 900px; overflow: hidden; }
  .backdrop {
    position: absolute; inset: 0;
    background: linear-gradient(160deg, #fbfbfc 0%, #f3f4f6 45%, #eceef1 100%);
  }
  .slide-title {
    position: absolute; left: 24px; top: 34px;
    font-size: 33px; font-weight: 700; color: var(--ink); line-height: 1;
  }
  .slide-title .accent { color: var(--brand-blue); }
  .title-rule {
    position: absolute; left: 0; top: 68px; width: 260px; height: 3px;
    background: var(--brand-blue);
  }
  .brand {
    position: absolute; right: 48px; top: 28px;
    display: flex; align-items: center; gap: 10px;
  }
  .brand-square { width: 26px; height: 26px; background: var(--mark-blue); }
  .brand-name { font-size: 21px; font-weight: 600; color: var(--mark-blue); }
  .content { position: absolute; left: 81px; top: 176px; width: 532px; }
  .subtitle { font-size: 25px; font-weight: 600; color: var(--brand-blue); line-height: 1.2; margin-bottom: 2px; }
  .content p { font-size: 20.5px; font-weight: 300; color: var(--body-text); line-height: 30px; margin-bottom: 30px; }
  .content p strong { font-weight: 700; color: var(--brand-blue); }
  .ring-chart { position: absolute; left: 0; top: 0; width: 1200px; height: 900px; }
  .ring-chart path { stroke: var(--white); stroke-width: 1.5; }
  .center-mark {
    position: absolute; left: 862px; top: 388px; width: 150px;
    display: flex; flex-direction: column; align-items: center; gap: 8px; text-align: center;
  }
  .center-mark .brand-square { width: 30px; height: 30px; }
  .center-mark .brand-name { font-size: 20px; line-height: 1.1; }
  .footer {
    position: absolute; left: 0; bottom: 0; width: 1200px; height: 57px;
    background: var(--footer-blue); display: flex; align-items: center; padding-left: 20px;
  }
  .footer-text { color: var(--white); font-size: 19px; font-weight: 400; }
</style>
</head>
<body>
<div class="slide">
  <div class="backdrop" role="img" aria-label="Faint photograph of glass office towers"></div>

  <h1 class="slide-title"><span class="accent">Slide</span> Title Here</h1>
  <div class="title-rule"></div>

  <div class="brand">
    <span class="brand-square"></span>
    <span class="brand-name">Ashcombe Holdings</span>
  </div>

  <section class="content">
    <h2 class="subtitle">Subtitle Here</h2>
    <p>Lorem ipsum dolor sit amet, consectetur adipiscing elit, sed do eiusmod tempor incididunt ut labore et dolore magna aliqua. Ut enim ad minim <strong>veniam, quis nostrud exercitation. Lorem ipsum dolor sit amet.</strong></p>
    <p>Consectetur adipiscing elit, sed do eiusmod tempor incididunt ut labore et dolore magna aliqua. Ut enim ad minim veniam, quis nostrud exercitation.</p>
    <p>Consectetur adipiscing elit, sed do eiusmod tempor incididunt ut labore et dolore magna aliqua. Ut enim ad minim veniam, quis nostrud exercitation.Consectetur adipiscing elit, sed do eiusmod tempor incididunt ut labore et dolore magna aliqua. Ut enim ad minim veniam, quis nostrud exercitation.</p>
  </section>

  <svg class="ring-chart" viewBox="0 0 800 600" aria-hidden="true">
    <g class="outer-ring">
      <path fill="var(--teal)" d="M625,134 A160,160 0 0 1 738.1,180.9 L715.5,203.5 A128,128 0 0 0 625,166 Z"/>
      <path fill="var(--mid-gray)" d="M511.9,180.9 A160,160 0 0 1 625,134 L625,166 A128,128 0 0 0 534.5,203.5 Z"/>
      <path fill="var(--dark-gray)" d="M465,294 A160,160 0 0 1 511.9,180.9 L534.5,203.5 A128,128 0 0 0 497,294 Z"/>
      <path fill="var(--navy)" d="M511.9,407.1 A160,160 0 0 1 465,294 L497,294 A128,128 0 0 0 534.5,384.5 Z"/>
      <path fill="var(--ocean)" d="M625,454 A160,160 0 0 1 511.9,407.1 L534.5,384.5 A128,128 0 0 0 625,422 Z"/>
      <path fill="var(--teal)" d="M738.1,407.1 A160,160 0 0 1 625,454 L625,422 A128,128 0 0 0 715.5,384.5 Z"/>
    </g>
    <g class="inner-ring">
      <path fill="var(--charcoal)" d="M569,197 A112,112 0 0 1 681,197 L661,231.6 A72,72 0 0 0 589,231.6 Z"/>
      <path fill="var(--inner-gray)" d="M501,294 A124,124 0 0 1 563,186.6 L589,231.6 A72,72 0 0 0 553,294 Z"/>
      <path fill="var(--deep-teal)" d="M563,401.4 A124,124 0 0 1 501,294 L553,294 A72,72 0 0 0 589,356.4 Z"/>
      <path fill="var(--teal)" d="M687,401.4 A124,124 0 0 1 563,401.4 L589,356.4 A72,72 0 0 0 661,356.4 Z"/>
    </g>
  </svg>

  <div class="center-mark">
    <span class="brand-square"></span>
    <span class="brand-name">Ashcombe<br>Holdings</span>
  </div>

  <footer class="footer">
    <span class="footer-text">Copyright text here</span>
  </footer>
</div>
</body>
</html>
```